Legal Information Website

We need a website that will serve as a source of information for people visiting, living, and working in the United Arab Emirates, where they can go and read about legal issues, laws, crimes, and most important find legal advice and find lawyers. The following are the pages of the website:

Find a Lawyer (Home Page)
This main feature of this page should be "Find a Lawyer"
Find a Lawyer should include the searching option by practice, by lawyer’s name, by law firm name or by location.

Ask a lawyer
This function allows the user to ask a lawyer a legal question and get an answer directly from a lawyer.

Research a legal matter
This function allows the user to do research on a certain legal topic. He/she can select from different legal topics.

Contact Us:
This page should include our contact details for the visitors in case they need any assistance. Contact us by Phone, Email, or Chat.

Once the design is approved, we will provide the rest of the website text.

Target Market(s)

General Public who seek legal advice

Industry/Entity Type

Law Firm

Font styles to use
Serif
Sans Serif

Requirements
Must have
• A tool to search for lawyer's, and then display the lawyer's picture and profile and credentials.

```html
<!DOCTYPE html>
<html lang="en">
<head>
<meta charset="utf-8">
<title>LexHaven – Find a Lawyer</title>
<link rel="stylesheet" href="https://fonts.googleapis.com/css2?family=Gelasio:wght@400;500&family=Open+Sans:wght@400;600;700&display=swap">
<style>
:root{
  --blue:#1f86d6;
  --blue-dark:#0f63ac;
  --blue-light:#3fa3ea;
  --navy:#1b3f6d;
  --link:#1668b8;
  --ink:#333;
  --muted:#8a8f95;
  --line:#e1e4e8;
  --dark:#2d2d2e;
  --footer:#2a2a2b;
  --page:#ffffff;
  --serif:'Gelasio', Georgia, serif;
  --sans:'Open Sans', Arial, sans-serif;
}
*{box-sizing:border-box;margin:0;padding:0}
html,body{width:939px;height:1200px;overflow:hidden;background:var(--page)}
.page{position:relative;width:939px;height:1200px;overflow:hidden;font-family:var(--sans);color:var(--ink)}
.abs{position:absolute}

/* header */
.brand{left:129px;top:18px;font-family:var(--serif);font-size:22px;color:var(--navy);display:flex;align-items:center;gap:8px;letter-spacing:.3px}
.brand-mark{width:12px;height:12px;background:var(--navy)}
.lang{left:744px;top:2px;font-size:7px;letter-spacing:.5px;color:#555;display:flex;align-items:center;gap:4px}
.lang svg{display:block}
.call-label{left:595px;top:23px;font-size:6.5px;letter-spacing:.6px;color:#444}
.help{left:482px;top:32px;font-family:var(--serif);font-size:13px;color:#333;display:flex;align-items:center;gap:6px}
.help b{font-family:var(--sans);font-weight:400;color:var(--link);font-size:12.5px}
.help-icon{width:13px;height:13px;background:var(--blue);border-radius:2px;display:flex;align-items:center;justify-content:center}
.chat{left:705px;top:18px;width:116px;height:35px;border:1px solid var(--line);background:#fff;box-shadow:0 1px 2px rgba(0,0,0,.08)}
.chat-title{position:absolute;left:10px;top:3px;font-family:var(--serif);font-size:13px;color:#333}
.chat-sub{position:absolute;left:10px;top:21px;font-size:7.5px;color:var(--link)}
.chat-photo{position:absolute;right:0;top:0;width:38px;height:33px;background:linear-gradient(135deg,#e9eef4,#c9a88f)}

/* nav */
.nav{left:0;top:63px;width:939px;height:32px;background:linear-gradient(#2f95df,#1670c0);border-bottom:1px solid #0d5ea3}
.nav a{position:absolute;top:0;height:32px;line-height:32px;text-align:center;color:#fff;text-decoration:none;font-family:var(--serif);font-size:12px;font-variant:small-caps;border-right:1px solid rgba(0,0,0,.15);box-shadow:1px 0 0 rgba(255,255,255,.12)}
.nav a.active{background:linear-gradient(#4fb0f0,#2a8ad6)}

/* hero */
.hero{left:0;top:95px;width:939px;height:268px;background:linear-gradient(90deg,#3b3d36 0%,#6d6a62 30%,#8f8b84 55%,#5e5d5c 75%,#a9aaa8 100%)}
.hero-title{left:127px;top:160px;font-family:var(--serif);font-size:39px;color:#fff;text-shadow:0 2px 4px rgba(0,0,0,.4)}
.hero-sub{left:131px;top:221px;font-size:16px;line-height:25px;color:#fff;text-shadow:0 1px 3px rgba(0,0,0,.5)}
.dots{display:flex;gap:6px}
.dots i{width:5px;height:5px;border-radius:50%;background:rgba(255,255,255,.5)}
.dots i.on{background:#fff}
.dots.light i{background:#dde0e4}
.dots.light i.on{background:#c3c7cc}

/* quick panels */
.band{left:0;top:363px;width:939px;height:58px;background:linear-gradient(#45a8ee,#2186d8)}
.quick{position:absolute;top:0;height:58px;padding:10px 0 0 20px;border-left:1px solid rgba(255,255,255,.15);border-right:1px solid rgba(0,0,0,.08)}
.quick.active{background:linear-gradient(#2b8cdc,#1566b3)}
.quick h3{font-family:var(--serif);font-weight:400;font-size:14.5px;color:#fff}
.quick p{font-size:10px;color:#dbeeff;margin-top:4px}
.caret{display:inline-block;width:0;height:0;border-left:3px solid transparent;border-right:3px solid transparent;border-top:4px solid currentColor;margin-left:4px;vertical-align:2px}
.pointer{left:153px;top:420px;width:0;height:0;border-left:8px solid transparent;border-right:8px solid transparent;border-top:8px solid #1566b3}

/* search */
.search{left:0;top:421px;width:939px;height:44px;background:var(--dark)}
.field{position:absolute;top:13px;width:157px;height:20px;background:#fff;border:1px solid #ccc;font-size:7.5px;color:#999;padding:5px 8px}
.search-btn{position:absolute;left:712px;top:12px;width:101px;height:22px;background:linear-gradient(#2f95df,#1670c0);border:1px solid #0d5ea3;color:#fff;font-size:7.5px;font-weight:700;display:flex;align-items:center;justify-content:center;gap:5px}

/* lawyers */
.section-title{font-family:var(--serif);font-size:14.5px;color:#333}
.card{position:absolute;top:516px;width:154px;height:192px;border:1px solid var(--line);background:#fff}
.card-photo{height:109px;background:linear-gradient(#eef0f2,#d4d8dc)}
.card h4{font-size:8.5px;color:var(--link);margin:13px 0 0 11px;font-weight:700}
.card p{font-size:7px;line-height:13px;color:var(--muted);margin:3px 10px 0 11px}
.sep{left:125px;top:745px;width:688px;height:4px;background:repeating-linear-gradient(90deg,#dfe2e5 0 1px,#f2f3f4 1px 2px)}

/* why */
.video{left:125px;top:777px;width:325px;height:194px;background:linear-gradient(120deg,#d8d2c9,#b7ada2 45%,#8d949c)}
.video-bar{position:absolute;left:0;bottom:0;width:100%;height:13px;background:#1b1b1b}
.video-track{position:absolute;left:0;top:-3px;width:100%;height:3px;background:#555}
.video-track::before{content:"";position:absolute;left:0;top:0;width:14px;height:3px;background:#d9282d}
.video-time{position:absolute;left:34px;top:3px;font-size:4.5px;color:#ccc}
.why-title{left:482px;top:776px}
.why-text{left:481px;top:806px;width:327px;font-size:6.6px;line-height:11.7px;color:var(--muted)}
.checks{position:absolute;top:880px;list-style:none}
.checks li{height:17.7px;font-size:6.5px;color:var(--muted);display:flex;align-items:center;gap:5px}
.tick{width:8px;height:8px;border-radius:50%;background:var(--blue);display:flex;align-items:center;justify-content:center;flex:none}

/* features */
.feature{position:absolute;top:1007px;width:218px;height:92px;background:linear-gradient(#f9fafb,#eceef0);box-shadow:0 10px 12px -8px rgba(0,0,0,.18)}
.feature h3{position:absolute;left:16px;top:28px;font-family:var(--serif);font-weight:400;font-size:14.5px;color:#333}
.feature p{position:absolute;left:17px;top:49px;font-size:10px;color:var(--link)}
.feature-art{position:absolute;right:0;top:0;height:92px}
.flags{position:absolute;left:120px;top:32px;display:flex;gap:8px}

/* footer */
.footer{left:0;top:1142px;width:939px;height:58px;background:var(--footer)}
.footer-brand{position:absolute;left:125px;top:18px;font-family:var(--serif);font-size:18px;color:#6b6b6c;display:flex;align-items:center;gap:6px}
.footer-brand i{width:10px;height:10px;background:#6b6b6c}
.footer-item{position:absolute;top:24px;font-size:7px;color:#c9c9c9;display:flex;align-items:center;gap:5px}
.social{position:absolute;top:21px;width:14px;height:14px;border-radius:50%;background:#555}
</style>
</head>
<body>
<div class="page">

  <header>
    <div class="abs brand"><span class="brand-mark"></span>LexHaven</div>
    <div class="abs lang">LANGUAGE:
      <svg width="13" height="9" viewBox="0 0 60 40" aria-label="English"><rect width="60" height="40" fill="#012169"/><path d="M0 0L60 40M60 0L0 40" stroke="#fff" stroke-width="8"/><path d="M0 0L60 40M60 0L0 40" stroke="#c8102e" stroke-width="3"/><path d="M30 0V40M0 20H60" stroke="#fff" stroke-width="12"/><path d="M30 0V40M0 20H60" stroke="#c8102e" stroke-width="7"/></svg>
      <svg width="13" height="9" viewBox="0 0 60 40" aria-label="Arabic"><rect width="60" height="40" fill="#fff"/><rect width="60" height="13.3" fill="#00732f"/><rect y="26.7" width="60" height="13.3" fill="#000"/><rect width="16" height="40" fill="#ff0000"/></svg>
    </div>
    <div class="abs call-label" style="left:595px">CALL US 24/7 HELPLINE</div>
    <div class="abs help"><span class="help-icon"><svg width="8" height="8" viewBox="0 0 24 24"><path fill="#fff" d="M6.6 10.8a15 15 0 006.6 6.6l2.2-2.2a1 1 0 011-.25 11.4 11.4 0 003.6.6 1 1 0 011 1V20a1 1 0 01-1 1A17 17 0 013 4a1 1 0 011-1h3.5a1 1 0 011 1 11.4 11.4 0 00.6 3.6 1 1 0 01-.25 1z"/></svg></span>Get Help Now: <b>+971 02 555 0147</b></div>
    <div class="abs chat">
      <div class="chat-title">Live Chat</div>
      <div class="chat-sub">&#9679; Online Now</div>
      <div class="chat-photo" role="img" aria-label="Photo of a support agent with headset"></div>
    </div>
  </header>

  <nav class="abs nav">
    <a class="active" style="left:129px;width:84px">Home</a>
    <a style="left:213px;width:138px">Find a Lawyer</a>
    <a style="left:351px;width:133px">Ask a Lawyer</a>
    <a style="left:484px;width:198px">Research a Legal Matter</a>
    <a style="left:682px;width:133px">Contact Us</a>
  </nav>

  <section class="abs hero" role="img" aria-label="Photo of businessmen in suits talking at a meeting"></section>
  <h1 class="abs hero-title" style="font-weight:400">Find a Lawyer.</h1>
  <p class="abs hero-sub">Your #1 source for finding the best<br>lawyers in the city.</p>
  <div class="abs dots" style="left:449px;top:346px"><i class="on"></i><i></i><i></i><i></i></div>

  <section class="abs band">
    <div class="quick active" style="left:126px;width:217px"><h3>Have An Urgent Problem?</h3><p style="color:#fff">Find a Lawyer now<span class="caret"></span></p></div>
    <div class="quick" style="left:345px;width:250px"><h3>Looking for information?</h3><p>Research Legal Advice<span class="caret"></span></p></div>
    <div class="quick" style="left:597px;width:216px"><h3>Didn’t find an answer?</h3><p>Ask a Lawyer for FREE<span class="caret"></span></p></div>
  </section>

  <section class="abs search">
    <div class="field" style="left:185px">Lawyer’s First Name</div>
    <div class="field" style="left:359px">Lawfirm Name</div>
    <div class="field" style="left:538px">By Location</div>
    <div class="search-btn"><svg width="7" height="7" viewBox="0 0 12 12"><circle cx="5" cy="5" r="3.5" fill="none" stroke="#fff" stroke-width="1.6"/><path d="M7.6 7.6L11 11" stroke="#fff" stroke-width="1.8"/></svg>SEARCH NOW</div>
  </section>
  <div class="abs pointer"></div>

  <h2 class="abs section-title" style="left:0;width:939px;text-align:center;top:482px;font-weight:400">Our Lawyers</h2>

  <article class="card" style="left:125px"><div class="card-photo" role="img" aria-label="Portrait of a female lawyer"></div><h4>Atty. Sarah Collins</h4><p>Lorem ipsum dolor sit amet, teft consecte tur adipiscing elit ut eunt nisl quis augue.</p></article>
  <article class="card" style="left:305px"><div class="card-photo" role="img" aria-label="Portrait of a male lawyer"></div><h4>Atty. Mark Bennett</h4><p>Lorem ipsum dolor sit amet, teft consecte tur adipiscing elit ut eunt nisl quis augue.</p></article>
  <article class="card" style="left:481px"><div class="card-photo" role="img" aria-label="Portrait of a female lawyer"></div><h4>Atty. Laura Hayes</h4><p>Lorem ipsum dolor sit amet, teft consecte tur adipiscing elit ut eunt nisl quis augue.</p></article>
  <article class="card" style="left:659px"><div class="card-photo" role="img" aria-label="Portrait of a senior male lawyer"></div><h4>Atty. David Turner</h4><p>Lorem ipsum dolor sit amet, teft consecte tur adipiscing elit ut eunt nisl quis augue.</p></article>
  <div class="abs dots light" style="left:449px;top:726px"><i class="on"></i><i></i><i></i><i></i></div>

  <div class="abs sep"></div>

  <div class="abs video" role="img" aria-label="Video still of a lawyer consulting with clients at a laptop">
    <div class="video-bar"><div class="video-track"></div><span class="video-time">0:02 / 4:17</span></div>
  </div>
  <h2 class="abs section-title why-title" style="font-weight:400">Why Choose LexHaven?</h2>
  <p class="abs why-text">Maecenas bibendum lacus gravida placerat consequat. Vivamus quis hendrerit mauris. Vestibulum laoreet felis sed consectetur sollicitudin. Sed a mauris massa. Nullam interdum, elit nec facilisis iaculis, arcu enim condimentum tellus, ut convallis elit purus eu est. Interdum et malesuada fames ac ante ipsum primis in faucibus. Nullam odio nulla, commodo a dui at, pretium iaculis quam. Pellentesque nec pellentesque metus. Curabitur id ligula velit. Pellentesque diam magna, sagittis .nec</p>
  <ul class="checks" style="left:480px">
    <li><span class="tick"><svg width="5" height="5" viewBox="0 0 10 10"><path d="M2 5l2 2 4-4" stroke="#fff" stroke-width="1.8" fill="none"/></svg></span>Maecenas bibendum lacus</li>
    <li><span class="tick"><svg width="5" height="5" viewBox="0 0 10 10"><path d="M2 5l2 2 4-4" stroke="#fff" stroke-width="1.8" fill="none"/></svg></span>Gravida placerat consequat</li>
    <li><span class="tick"><svg width="5" height="5" viewBox="0 0 10 10"><path d="M2 5l2 2 4-4" stroke="#fff" stroke-width="1.8" fill="none"/></svg></span>Vivamus quis hendrerit</li>
    <li><span class="tick"><svg width="5" height="5" viewBox="0 0 10 10"><path d="M2 5l2 2 4-4" stroke="#fff" stroke-width="1.8" fill="none"/></svg></span>Mauris Vestibulum laoreet</li>
    <li><span class="tick"><svg width="5" height="5" viewBox="0 0 10 10"><path d="M2 5l2 2 4-4" stroke="#fff" stroke-width="1.8" fill="none"/></svg></span>Felis sed consectetur sollictn</li>
  </ul>
  <ul class="checks" style="left:597px">
    <li><span class="tick"><svg width="5" height="5" viewBox="0 0 10 10"><path d="M2 5l2 2 4-4" stroke="#fff" stroke-width="1.8" fill="none"/></svg></span>Maecenas bibendum lacus</li>
    <li><span class="tick"><svg width="5" height="5" viewBox="0 0 10 10"><path d="M2 5l2 2 4-4" stroke="#fff" stroke-width="1.8" fill="none"/></svg></span>Gravida placerat consequat</li>
    <li><span class="tick"><svg width="5" height="5" viewBox="0 0 10 10"><path d="M2 5l2 2 4-4" stroke="#fff" stroke-width="1.8" fill="none"/></svg></span>Vivamus quis hendrerit Mauris</li>
    <li><span class="tick"><svg width="5" height="5" viewBox="0 0 10 10"><path d="M2 5l2 2 4-4" stroke="#fff" stroke-width="1.8" fill="none"/></svg></span>Vestibulum laoreet Felis sed</li>
    <li><span class="tick"><svg width="5" height="5" viewBox="0 0 10 10"><path d="M2 5l2 2 4-4" stroke="#fff" stroke-width="1.8" fill="none"/></svg></span>consectetur sollictn Sed a</li>
  </ul>

  <article class="feature" style="left:125px">
    <div class="feature-art" role="img" aria-label="Photo of the legal team standing in suits" style="width:96px;background:linear-gradient(90deg,rgba(236,238,240,0),#9a9ea4 40%,#4a4d52)"></div>
    <h3>Meet LexHaven Team</h3><p>+17 Years Experience</p>
  </article>
  <article class="feature" style="left:361px">
    <div class="feature-art" role="img" aria-label="Photo of a smiling support agent with headset" style="width:96px;background:linear-gradient(90deg,rgba(236,238,240,0),#d8b79f 50%,#a97b5e)"></div>
    <h3>Chat Live Now</h3><p>24 Hours 7 Days a week</p>
  </article>
  <article class="feature" style="left:597px">
    <div class="feature-art" role="img" aria-label="Faint world map background" style="width:150px;background:linear-gradient(90deg,rgba(236,238,240,0),#e2e5e8)"></div>
    <h3>We Speak</h3><p>Arabic &amp; English</p>
    <div class="flags">
      <svg width="36" height="27" viewBox="0 0 60 45" aria-label="English"><rect width="60" height="45" fill="#012169"/><path d="M0 0L60 45M60 0L0 45" stroke="#fff" stroke-width="9"/><path d="M0 0L60 45M60 0L0 45" stroke="#c8102e" stroke-width="3"/><path d="M30 0V45M0 22.5H60" stroke="#fff" stroke-width="14"/><path d="M30 0V45M0 22.5H60" stroke="#c8102e" stroke-width="8"/></svg>
      <svg width="36" height="27" viewBox="0 0 60 45" aria-label="Arabic"><rect width="60" height="45" fill="#fff"/><rect width="60" height="15" fill="#00732f"/><rect y="30" width="60" height="15" fill="#000"/><rect width="17" height="45" fill="#ff0000"/></svg>
    </div>
  </article>

  <footer class="abs footer">
    <div class="footer-brand"><i></i>LexHaven</div>
    <div class="footer-item" style="left:366px"><svg width="8" height="6" viewBox="0 0 16 12"><rect width="16" height="12" fill="#999"/><path d="M0 0l8 6 8-6" stroke="#2a2a2b" stroke-width="1.5" fill="none"/></svg>contact@lexhaven.com</div>
    <div class="footer-item" style="left:485px"><svg width="7" height="7" viewBox="0 0 24 24"><path fill="#999" d="M6.6 10.8a15 15 0 006.6 6.6l2.2-2.2a1 1 0 011-.25 11.4 11.4 0 003.6.6 1 1 0 011 1V20a1 1 0 01-1 1A17 17 0 013 4a1 1 0 011-1h3.5a1 1 0 011 1 11.4 11.4 0 00.6 3.6 1 1 0 01-.25 1z"/></svg>(Toll FREE) +123 555 0190</div>
    <div class="footer-item" style="left:600px">Copyright 2014. LexHaven | All Rights Reserved</div>
    <span class="social" style="left:774px"></span>
    <span class="social" style="left:797px"></span>
  </footer>

</div>
</body>
</html>
```